Lionel Varkestone and Dennis Holtby Advertisement

We would like an ad that conveys understated elegance. We are a company that purchases estate jewelry watches and diamonds. We care to a wealthy, upscale clientele.

Target Market(s)

Wealthy upscale.

Industry/Entity Type

It Company

Requirements
Must have
• Elegant Design. Crisp Clean. Attached a doc of how the ad should be arranged.

```html
<!DOCTYPE html>
<html lang="en">
<head>
<meta charset="utf-8">
<title>Lionel Varkestone &amp; Dennis Holtby — Advertisement</title>
<link rel="stylesheet" href="https://fonts.googleapis.com/css2?family=Cinzel:wght@400;500&family=Open+Sans:wght@600&display=swap">
<style>
  :root {
    --paper-top: #e6e6e6;
    --paper-mid: #fbfbfb;
    --band-light: #d6d6d6;
    --band-mid: #a9a9a9;
    --band-dark: #7a7a7a;
    --ring-dark: #1c1c1c;
    --ring-light: #d9d9d9;
    --ink: #3a3a3a;
    --ink-soft: #4f4f4f;
    --white: #ffffff;
  }
  * { margin: 0; padding: 0; box-sizing: border-box; }
  html, body { width: 848px; height: 1200px; overflow: hidden; background: var(--white); }
  .ad {
    position: relative;
    width: 848px;
    height: 1200px;
    overflow: hidden;
    background: linear-gradient(180deg, var(--paper-top) 0%, var(--paper-mid) 45%, #f3f3f3 68%, var(--band-light) 78%, var(--band-mid) 90%, var(--band-dark) 100%);
  }
  .hero-frame { position: absolute; left: 0; top: 0; }
  .brand__mark {
    position: absolute;
    left: 394px; top: 770px;
    width: 60px; height: 60px;
    border: 2px solid var(--ink);
    border-radius: 50%;
  }
  .brand__name {
    position: absolute;
    left: 0; right: 0; top: 866px;
    text-align: center;
    font-family: "Cinzel", serif;
    font-weight: 400;
    font-size: 25px;
    line-height: 30px;
    letter-spacing: 0.4px;
    color: var(--ink);
  }
  .brand__tagline {
    position: absolute;
    left: 0; right: 0; top: 902px;
    display: flex;
    align-items: center;
    justify-content: center;
    gap: 10px;
    font-family: "Cinzel", serif;
    font-size: 12.5px;
    line-height: 16px;
    letter-spacing: 1px;
    color: var(--ink);
  }
  .brand__rule { width: 150px; height: 1.5px; background: var(--ink); }
  .contact {
    position: absolute;
    left: 0; right: 0;
    text-align: center;
    font-family: "Open Sans", sans-serif;
    font-weight: 600;
    color: var(--ink-soft);
  }
  .contact__address { top: 958px; font-size: 21px; line-height: 30px; font-style: normal; }
  .contact__email { top: 1064px; font-size: 18px; line-height: 24px; }
  .contact__call {
    top: 1116px;
    font-family: "Cinzel", serif;
    font-weight: 500;
    font-size: 39px;
    line-height: 46px;
    letter-spacing: 0.5px;
    color: var(--white);
  }
</style>
</head>
<body>
<main class="ad">
  <svg class="hero-frame" width="848" height="760" viewBox="0 0 848 760">
    <defs>
      <linearGradient id="ring-metal" x1="0" y1="0" x2="1" y2="0.3">
        <stop offset="0" stop-color="var(--ring-dark)"/>
        <stop offset="0.35" stop-color="#6a6a6a"/>
        <stop offset="0.55" stop-color="var(--ring-light)"/>
        <stop offset="0.8" stop-color="#4a4a4a"/>
        <stop offset="1" stop-color="var(--ring-dark)"/>
      </linearGradient>
      <radialGradient id="inner-white" cx="0.5" cy="0.45" r="0.6">
        <stop offset="0" stop-color="#ffffff"/>
        <stop offset="1" stop-color="#e9e9e9"/>
      </radialGradient>
      <radialGradient id="gem-tone" cx="0.5" cy="0.5" r="0.6">
        <stop offset="0" stop-color="#ffffff"/>
        <stop offset="0.7" stop-color="#dcdcdc"/>
        <stop offset="1" stop-color="#b8b8b8"/>
      </radialGradient>
    </defs>
    <circle class="hero-frame__ring" cx="448" cy="372" r="318" fill="url(#ring-metal)"/>
    <circle class="hero-frame__lip" cx="444" cy="376" r="292" fill="#f5f5f5"/>
    <circle class="hero-frame__inner" cx="444" cy="376" r="286" fill="url(#inner-white)" stroke="#9a9a9a" stroke-width="1.5"/>
    <rect class="hero-frame__gem" x="264" y="232" width="356" height="352" rx="30"
          fill="url(#gem-tone)" role="img" aria-label="Photograph of a loose emerald-cut diamond"/>
  </svg>

  <span class="brand__mark" aria-hidden="true"></span>
  <h1 class="brand__name">Lionel Varkestone &amp; Dennis Holtby</h1>
  <p class="brand__tagline">
    <span class="brand__rule"></span>YOUR BEST OPTION<span class="brand__rule"></span>
  </p>

  <address class="contact contact__address">
    Casa Lumière<br>
    318-B Alder Promenade<br>
    Coral Haven, FL 33497
  </address>
  <p class="contact contact__email">concierge@varkestoneholtby.com</p>
  <p class="contact contact__call">CALL US NOW: 561.555.0147</p>
</main>
</body>
</html>
```